Corvanta Business cards template

We're looking for something modern and elegant. We are a reseller of technology (computers, datacenter, etc). Color theme would be "only" white with the incorporation of the blue that's present on our website (Corvanta.com) and logo file. We would like for the card to provide all the necessary info for the specific person (Phone#, fax#, email, name, website URL) . I'm attaching the logo file to this request. Please have it show Montreal/New York somewhere, without providing specific addresses.

Target Market(s)

All b2b

Industry/Entity Type

Business

Contact Information for Business Card

Please have the color scheme be represented by only the white and blue from our website (Corvanta.com) and logo. We would like to logo on the card, but not big and overwhelming. This card will be used as a template for anybody within the company, it should display the user's name, phone#, fax#, email, job title and website URL. Please have it show Montreal/New York somewhere, without providing our specific addresses. Really, we're looking for a clean, simple and elegant look.

Font styles to use
Serif

Requirements
Must have
• Please see card details
Nice to have
• Please see card details
Should not have
• Anything tacky or tagline.

```html
<!DOCTYPE html>
<html lang="en">
<head>
<meta charset="utf-8">
<title>Corvanta Business Cards</title>
<link rel="stylesheet" href="https://fonts.googleapis.com/css2?family=Lora:wght@400;500;700&display=swap">
<style>
  :root{
    --stage:#2b2e33;
    --card:#ffffff;
    --blue:#1b79c4;
    --blue-light:#3d9be0;
    --blue-deep:#1565a8;
    --ink:#1d1d1f;
  }
  *{box-sizing:border-box;margin:0;padding:0}
  html,body{width:1200px;height:900px;overflow:hidden}
  body{background:var(--stage);font-family:"Lora",serif;position:relative}

  .card{position:absolute;background:var(--card);border-radius:24px;overflow:hidden;
        box-shadow:0 18px 40px rgba(0,0,0,.45)}

  /* Front, vertical */
  .card-front{left:130px;top:160px;width:370px;height:600px}
  .front-wordmark{position:absolute;left:40px;top:62px;font-size:46px;font-weight:500;
        color:var(--blue);letter-spacing:.5px;line-height:1.1}
  .holder{position:absolute;left:40px;top:146px}
  .holder-name{font-size:34px;font-weight:400;color:var(--ink);line-height:1.15}
  .holder-name .first{color:var(--blue);font-weight:700}
  .holder-title{font-size:15px;font-weight:500;color:var(--ink);margin-top:2px}

  .contact-list{position:absolute;left:40px;top:230px;list-style:none}
  .contact-item{display:flex;align-items:center;gap:14px;margin-bottom:12px;
        font-size:14px;font-weight:500;color:var(--ink);line-height:1.3}
  .contact-label{color:var(--blue);font-weight:700;display:inline-block;width:16px}
  .contact-icon{flex:0 0 30px;width:30px;height:30px;border-radius:50%;background:var(--blue-light);
        display:flex;align-items:center;justify-content:center}
  .contact-icon svg{width:16px;height:16px}
  .contact-cities{letter-spacing:.8px}

  .front-wave{position:absolute;left:0;bottom:0;width:370px;height:230px}

  /* Back, horizontal */
  .card-back{left:545px;top:150px;width:600px;height:360px}
  .back-brand{position:absolute;inset:0;display:flex;flex-direction:column;
        align-items:center;justify-content:center}
  .back-wordmark{font-size:64px;font-weight:500;color:var(--blue);letter-spacing:.5px;line-height:1.1}
  .back-url{font-size:20px;font-weight:500;color:var(--blue);margin-top:8px;letter-spacing:.5px}
</style>
</head>
<body>

<section class="card card-front" aria-label="Card front">
  <div class="front-wordmark">Corvanta</div>

  <div class="holder">
    <div class="holder-name"><span class="first">Your</span> Name</div>
    <div class="holder-title">Managing Director</div>
  </div>

  <ul class="contact-list">
    <li class="contact-item">
      <span class="contact-icon"><svg viewBox="0 0 24 24"><path fill="#fff" d="M6.6 10.8a15 15 0 0 0 6.6 6.6l2.2-2.2c.3-.3.7-.4 1-.2 1.1.4 2.3.6 3.6.6.6 0 1 .4 1 1V20c0 .6-.4 1-1 1A17 17 0 0 1 3 4c0-.6.4-1 1-1h3.5c.6 0 1 .4 1 1 0 1.3.2 2.5.6 3.6.1.3 0 .7-.2 1z"/></svg></span>
      <span><span class="contact-label">T</span> 1-855-555-0142<br><span class="contact-label">F</span> 1-855-555-0143</span>
    </li>
    <li class="contact-item">
      <span class="contact-icon"><svg viewBox="0 0 24 24" fill="none" stroke="#fff" stroke-width="2"><circle cx="12" cy="12" r="9"/><path d="M3 12h18M12 3c3 3 3 15 0 18M12 3c-3 3-3 15 0 18"/></svg></span>
      www.corvanta.com
    </li>
    <li class="contact-item">
      <span class="contact-icon"><svg viewBox="0 0 24 24" fill="none" stroke="#fff" stroke-width="2"><rect x="3" y="6" width="18" height="12" rx="1"/><path d="M3 7l9 6 9-6"/></svg></span>
      info@corvanta.com
    </li>
    <li class="contact-item">
      <span class="contact-icon"><svg viewBox="0 0 24 24"><path fill="#fff" d="M12 2a7 7 0 0 0-7 7c0 5 7 13 7 13s7-8 7-13a7 7 0 0 0-7-7zm0 9.5A2.5 2.5 0 1 1 12 6.5a2.5 2.5 0 0 1 0 5z"/></svg></span>
      <span class="contact-cities">MONTREAL | NEW YORK</span>
    </li>
  </ul>

  <svg class="front-wave" viewBox="0 0 370 230" preserveAspectRatio="none" aria-hidden="true">
    <path d="M0 200 C120 150 260 80 370 0 L370 230 L0 230 Z" fill="var(--blue-light)"/>
    <path d="M0 215 C130 170 270 100 370 30 L370 230 L0 230 Z" fill="var(--blue)"/>
    <path d="M0 225 C140 190 280 125 370 60 L370 230 L0 230 Z" fill="var(--blue-deep)"/>
  </svg>
</section>

<section class="card card-back" aria-label="Card back">
  <div class="back-brand">
    <div class="back-wordmark">Corvanta</div>
    <div class="back-url">www.corvanta.com</div>
  </div>
</section>

</body>
</html>
```